Brightwell Giving Inc

We need a full re-design of our non-profit organization website (www.brightwellgiving.org). Ideally, we are looking to make it more attractive, user-friendly, and interactive with our business model.

Please make sure to user colors that ago with our logo.

We need a homepage done and we also need a content page done where we will use for the other pages to fill with content.

Target Market(s)

Clothes/textiles donations.

Industry/Entity Type

Charity

Number of Pages Required

2 page

Colors

Designer to choose colors to be used in the design.

Requirements
Must have
• It must match the styling of our logo and same colors as current website. (www.brightwellgiving.org)
Nice to have
• Sleek homepage that is easy to understand and get our main points across.

```html
<!DOCTYPE html>
<html lang="en">
<head>
<meta charset="utf-8">
<title>Our Statement – Brightwell Giving</title>
<link href="https://fonts.googleapis.com/css2?family=Arvo:wght@400;700&family=Montserrat:wght@300;400;600;700&display=swap" rel="stylesheet">
<style>
:root{
  --green-dark:#5e8f3e;
  --green:#7ab648;
  --green-text:#6aab3a;
  --yellow:#f9bb00;
  --ink:#2b2b2b;
  --body:#444;
  --muted:#8a8a8a;
  --panel:#f2f2f2;
  --white:#fff;
}
*{box-sizing:border-box;margin:0;padding:0}
html,body{width:957px;height:1200px;overflow:hidden;background:var(--white)}
body{position:relative;font-family:"Montserrat",sans-serif;color:var(--body)}
.abs{position:absolute}
.topbar{left:0;top:0;width:957px;height:63px}
.brand{left:60px;top:18px;display:flex;align-items:center;gap:8px}
.brand-mark{width:24px;height:24px;background:var(--green);border-radius:50%}
.brand-name{font-family:"Montserrat",sans-serif;font-weight:600;font-size:15px;color:var(--green-dark);line-height:1}
.contact{right:59px;top:18px;font-size:9.5px;color:var(--ink);line-height:15.5px;text-align:left}
.contact b{font-weight:700}
.nav{left:0;top:63px;width:957px;height:32px;background:var(--green-dark)}
.nav ul{list-style:none;display:flex;position:absolute;left:60px;top:0;height:32px;align-items:center}
.nav li{color:var(--white);font-size:9.5px;margin-right:31px}
.nav li.active{font-weight:700}
.caret{display:inline-block;border:3px solid transparent;border-top:3.5px solid var(--white);border-bottom:0;margin-left:3px;vertical-align:middle}
.nav-donate{right:60px;top:0;width:84px;height:32px;background:var(--yellow);color:var(--white);font-weight:700;font-size:9.5px;display:flex;align-items:center;justify-content:center}
.hero{left:0;top:95px;width:957px;height:168px;background:linear-gradient(90deg,#7fb84d,#75b043 50%,#80b94f)}
.crumb{left:60px;top:135px;color:var(--white);font-size:9.5px}
.crumb b{font-weight:700}
.hero-title{left:56px;top:155px;font-family:"Arvo",serif;font-size:35px;color:var(--white);font-weight:400}
.main{left:60px;top:318px;width:512px}
.main h2{font-family:"Arvo",serif;font-weight:400;font-size:24px;color:var(--ink);margin-bottom:18px}
.main p{font-size:11.4px;letter-spacing:.15px;line-height:18.5px;margin-bottom:18.5px;font-weight:400}
.main h2.second{margin-top:22px}
.help{left:59px;top:910px;width:514px;height:169px;background:var(--panel);padding:25px 23px}
.help h3{font-family:"Arvo",serif;font-size:14px;color:var(--ink);margin-bottom:10px}
.help p{font-size:11.2px;line-height:18px;margin-bottom:18px}
.btn{display:inline-flex;align-items:center;justify-content:center;background:var(--yellow);color:var(--white);font-family:"Arvo",serif;font-weight:700;font-size:10px}
.help .btn{width:91px;height:36px}
.finder{left:628px;top:308px;width:270px;height:155px;background:var(--white);box-shadow:0 0 6px rgba(0,0,0,.12);padding:19px 13px 0}
.finder h4{font-family:"Arvo",serif;font-weight:400;font-size:13px;color:var(--ink);text-align:center;line-height:16px;margin:0 30px 13px}
.zip{height:36px;border:1px solid #cfcfcf;display:flex;align-items:center;justify-content:center;gap:4px;color:var(--muted);font-size:9.5px;margin-bottom:7px}
.finder .btn{width:100%;height:36px}
.news-title{left:629px;top:491px;font-family:"Arvo",serif;font-weight:400;font-size:16px;color:var(--ink)}
.news{left:629px;width:270px;border-left:2px solid var(--green);padding-left:17px}
.news h5{font-family:"Arvo",serif;font-weight:700;font-size:13.2px;line-height:18.5px;color:var(--ink);padding-top:5px;max-width:200px}
.news time{display:block;font-size:9.5px;color:var(--muted);margin:3px 0 12px}
.news p{font-size:11px;line-height:18px}
.news a{display:block;margin-top:14px;padding-bottom:8px;font-family:"Arvo",serif;font-weight:700;font-size:10px;color:var(--green-text);text-decoration:none}
.footer{left:0;top:1136px;width:957px;height:64px;background:var(--green-dark);color:var(--white)}
.seal{left:50px;top:1147px;width:40px;height:40px;border-radius:50%;background:#e6b62a}
.copy{left:102px;top:1161px;font-size:9.5px;color:var(--white)}
.flinks{right:112px;top:1161px;font-size:9.5px;color:var(--white)}
.flinks span{margin:0 4px}
.social{top:1159px;width:13px;height:13px;background:var(--white);border-radius:2px}
</style>
</head>
<body>
<header class="abs topbar">
  <div class="abs brand">
    <div class="brand-mark"></div>
    <div class="brand-name">Brightwell Giving</div>
  </div>
  <div class="abs contact"><b>Toll Free:</b> (855) 555-0148<br><b>New York:</b> 518-555-0173</div>
</header>
<nav class="abs nav">
  <ul>
    <li>Home</li>
    <li class="active">Missions<span class="caret"></span></li>
    <li>How It Works</li>
    <li>About Us<span class="caret"></span></li>
    <li>Sponsors</li>
    <li>News</li>
  </ul>
  <div class="abs nav-donate">Donate</div>
</nav>
<div class="abs hero" role="img" aria-label="Volunteers and children at a community clothing drive under a green tint"></div>
<div class="abs crumb">Missions&nbsp; / &nbsp;<b>Our Statment</b></div>
<h1 class="abs hero-title">Our Statement</h1>

<main class="abs main">
  <h2>Missions Statement</h2>
  <p>Brightwell Giving has a two part mission to help local communities while helping the planet. The average American discards 68 lbs of clothing annually. That is 1,325,340,196 lbs for New York State alone and 21,202,400,000 lbs for the U.S. every year!</p>
  <p>By keeping unwanted clothes out of the trash can we are greatly reducing the amount of material that enters our landfills. We are also turning the unwanted clothes into funding for our local communities. We are asking for your help to increase local support. Simply put, there is no better time to act than now.</p>
  <h2 class="second">Impact Statement</h2>
  <p>In such trying times as these, the only people we can turn to for help are each other. Nothing is greater than the desire of a community to help its own. Brightwell Giving is dedicated to becoming an active member of the community by providing for its less fortunate members.</p>
  <p>Our goal is to differentiate ourselves from other charitable organizations by running a transparent operation that makes the most of its donations. Our plan is to run an “open book” charity wherein all of our operations and accounting system are fully disclosed to the public. This will allow the community and its donors to see where your donations are going.</p>
  <p>Anyone will be able to review the operating costs of our organization in order to ensure that we are giving the most amount possible to the community’s beneficiaries. A non-profit organization is only effective when it benefits the people that need it most. With your help, we can accomplish that goal. Brightwell Giving aims to bring back the spirit of</p>
</main>

<section class="abs help">
  <h3>We need your help!</h3>
  <p>We have a great team here at Brightwell Giving, who have proven time and again that they’re capable of great things. However, we still rely on your help to get by.</p>
  <span class="btn">Donate</span>
</section>

<aside class="abs finder">
  <h4>Find your nearest donation point</h4>
  <div class="zip"><svg width="9" height="12" viewBox="0 0 9 12"><path d="M4.5 0A4.5 4.5 0 0 0 0 4.5C0 8 4.5 12 4.5 12S9 8 9 4.5A4.5 4.5 0 0 0 4.5 0zm0 6.3a1.8 1.8 0 1 1 0-3.6 1.8 1.8 0 0 1 0 3.6z" fill="#b5b5b5"/></svg>ZIP code</div>
  <span class="btn">Submit</span>
</aside>

<h3 class="abs news-title">Latest News</h3>
<article class="abs news" style="top:545px">
  <h5>We are starting the charity projects to collect funds on FundCircle</h5>
  <time>January 21st 2018</time>
  <p>Brightwell Giving created the flyer for inform the people in Manhattan to help others by giving donation.</p>
  <a href="#">Read more</a>
</article>
<article class="abs news" style="top:751px">
  <h5>We are starting the charity projects to collect funds on FundCircle</h5>
  <time>January 21st 2018</time>
  <p>Brightwell Giving created the flyer for inform the people in Manhattan to help others by giving donation.</p>
  <a href="#">Read more</a>
</article>

<footer class="abs footer"></footer>
<div class="abs seal"></div>
<div class="abs copy">Copyright © Brightwell Giving 2018</div>
<div class="abs flinks">Home<span>|</span>Missions<span>|</span>How it Works<span>|</span>About Us<span>|</span>Sponsors<span>|</span>News<span>|</span>Wall of Needs<span>|</span>Donate</div>
<div class="abs social" style="left:859px"></div>
<div class="abs social" style="left:884px;border-radius:50%"></div>
</body>
</html>
```